Business card for massage therapy company called Brook Fern Wellness

Need business card for massage therapy company called Brook Fern Wellness. Would like my logo on the front and the back of the card I have 3 options of logos and you can play with what looks better.

Would like this information displayed on the back of the card:

Marcus Ellery
Licensed Massage Therapist
321-555-0147
brookfern-example.com
brookfern_rest_

```html
<!DOCTYPE html>
<html lang="en">
<head>
<meta charset="utf-8">
<title>Brook Fern Wellness – Business Card</title>
<link href="https://fonts.googleapis.com/css2?family=Josefin+Sans:wght@300;400&family=Montserrat:wght@400;500&display=swap" rel="stylesheet">
<style>
  :root {
    --backdrop: #d9d9de;
    --card: #ffffff;
    --sage: #737c62;
    --clay: #b88a63;
    --ink: #2c2c2c;
  }
  * { box-sizing: border-box; margin: 0; padding: 0; }
  html, body { width: 1200px; height: 1129px; overflow: hidden; }
  body {
    background: var(--backdrop);
    position: relative;
    font-family: "Montserrat", sans-serif;
  }
  .card {
    position: absolute;
    left: 205px;
    width: 790px;
    height: 452px;
    background: var(--card);
    border-radius: 38px;
    overflow: hidden;
  }
  .card--front { top: 92px; }
  .card--back { top: 584px; }

  .brand {
    font-family: "Josefin Sans", sans-serif;
    font-weight: 400;
    color: var(--sage);
    text-transform: uppercase;
    line-height: 1;
    white-space: nowrap;
  }
  .brand__main { display: block; }
  .brand__sub { display: block; }

  /* front */
  .front__ring {
    position: absolute;
    left: 295px; top: 66px;
    width: 200px; height: 200px;
    border: 3px solid var(--sage);
    border-radius: 50%;
  }
  .card--front .brand {
    position: absolute;
    left: 0; right: 0; top: 288px;
    text-align: center;
  }
  .card--front .brand__main { font-size: 66px; letter-spacing: 4px; }
  .card--front .brand__sub { font-size: 30px; letter-spacing: 14px; margin-top: 20px; padding-left: 14px; }

  /* back */
  .card--back .brand {
    position: absolute;
    left: 38px; top: 58px;
    width: 300px;
    text-align: center;
  }
  .card--back .brand__main { font-size: 46px; letter-spacing: 3px; }
  .card--back .brand__sub { font-size: 24px; letter-spacing: 11px; margin-top: 16px; padding-left: 11px; }

  .accent-bar {
    position: absolute;
    left: 0; top: 187px;
    width: 19px; height: 69px;
    background: var(--sage);
  }
  .person {
    position: absolute;
    left: 38px; top: 186px;
  }
  .person__name {
    font-family: "Josefin Sans", sans-serif;
    font-weight: 300;
    font-size: 37px;
    letter-spacing: 1px;
    color: var(--ink);
    text-transform: uppercase;
    line-height: 1;
    white-space: nowrap;
  }
  .person__title {
    font-size: 20px;
    color: var(--clay);
    margin-top: 14px;
    letter-spacing: 0.5px;
    white-space: nowrap;
  }
  .contact {
    position: absolute;
    left: 38px; top: 300px;
    list-style: none;
  }
  .contact__item {
    display: flex;
    align-items: center;
    height: 37px;
    font-size: 20px;
    color: var(--ink);
    letter-spacing: 0.3px;
  }
  .contact__icon {
    width: 19px; height: 19px;
    margin-right: 9px;
    flex: none;
  }
  .contact__dot {
    width: 17px; height: 17px;
    border: 2px solid var(--sage);
    border-radius: 3px;
    margin-right: 10px;
    flex: none;
  }
  .back__ring {
    position: absolute;
    left: 387px; top: 54px;
    width: 344px; height: 344px;
    border: 4px solid var(--sage);
    border-radius: 50%;
  }
</style>
</head>
<body>
  <section class="card card--front">
    <div class="front__ring"></div>
    <h1 class="brand">
      <span class="brand__main">Brook Fern</span>
      <span class="brand__sub">Wellness</span>
    </h1>
  </section>

  <section class="card card--back">
    <h2 class="brand">
      <span class="brand__main">Brook Fern</span>
      <span class="brand__sub">Wellness</span>
    </h2>
    <div class="accent-bar"></div>
    <div class="person">
      <p class="person__name">Marcus&nbsp;&nbsp;Ellery</p>
      <p class="person__title">Licensed Massage Therapist</p>
    </div>
    <ul class="contact">
      <li class="contact__item">
        <svg class="contact__icon" viewBox="0 0 24 24" aria-hidden="true">
          <path d="M6.6 10.8a15 15 0 0 0 6.6 6.6l2.2-2.2a1 1 0 0 1 1-.25 11.4 11.4 0 0 0 3.6.57 1 1 0 0 1 1 1V20a1 1 0 0 1-1 1A17 17 0 0 1 3 4a1 1 0 0 1 1-1h3.5a1 1 0 0 1 1 1c0 1.25.2 2.45.57 3.57a1 1 0 0 1-.25 1z" fill="none" stroke="#2c2c2c" stroke-width="1.8"/>
          <path d="M14 3a7 7 0 0 1 7 7M14 6.5a3.5 3.5 0 0 1 3.5 3.5" fill="none" stroke="#2c2c2c" stroke-width="1.6"/>
        </svg>
        321-555-0147
      </li>
      <li class="contact__item">
        <svg class="contact__icon" viewBox="0 0 24 24" aria-hidden="true">
          <circle cx="12" cy="12" r="10" fill="#2c2c2c"/>
          <path d="M7 6c2 1 3 3 2 5s1 3 0 5M15 4c-1 2 1 3 3 4M14 14c2 0 3 2 2 5" fill="none" stroke="#fff" stroke-width="1.6"/>
        </svg>
        brookfern-example.com
      </li>
      <li class="contact__item">
        <span class="contact__dot"></span>
        brookfern_rest_
      </li>
    </ul>
    <div class="back__ring"></div>
  </section>
</body>
</html>
```